Admin Backend Redesign

We need a redesign for our backend which supoosed to make the backoffice look more modern!

I will add screenshots of the backoffice so you know what data will be shown in the Admin.

Have in mind that the users of this backend are Doctors. We need a clinical look, modern and sharp. The backoffice is responsive, have that in mind. We need the backoffice to look as professional as possible.

The theme used for the website is: http://velmora.brisk-sample.net/

ON the main page of the backoffice, under every widget i need some space to write an explanation what the widget is about.

The color code used in our logo and website is #57aad4 combined with white.

We are open for ideas!
Updates

Project Deadline Extended
Reason: Designs are ok, but nothing innovative. Please use more modern designs!

Project Deadline Extended
Reason: Havent recieved a perfect design yet. Please read instructions carefully! Thank you

Project Deadline Extended
Reason: Hey everybody, sorry for the delay. We will decide in 3 days. If anyone wants to add a Design, that would be great.

Target Market(s)

Doctors, therapists

Industry/Entity Type

It Professional

Font styles to use
Sans Serif

Requirements
Must have
• Must look uptodate, modern, like new back offices look nowadays

```html
<!DOCTYPE html>
<html lang="de">
<head>
<meta charset="utf-8">
<title>Medirate Dashboard</title>
<link href="https://fonts.googleapis.com/css2?family=Raleway:wght@400;500;600&family=Open+Sans:wght@400;600&display=swap" rel="stylesheet">
<style>
:root{
  --topbar:#1f1f1f;
  --sidebar:#3a3a3a;
  --footer:#2b2b2b;
  --teal:#35cfcf;
  --teal-dark:#2cbcbc;
  --blue:#2e5fb0;
  --blue-dark:#234f98;
  --panel-head:#9b9b9b;
  --panel-body:#f7f7f7;
  --crumb:#ececec;
  --text:#555;
  --muted:#999;
  --link:#2a5aa8;
  --green:#1e9a3c;
  --star:#f0a830;
}
*{box-sizing:border-box;margin:0;padding:0}
html,body{width:883px;height:1200px;overflow:hidden}
body{position:relative;background:#fff;font-family:'Open Sans',sans-serif;color:var(--text);font-size:8px}
.topbar{position:absolute;left:0;top:0;width:883px;height:58px;background:var(--topbar)}
.user{position:absolute;right:32px;top:14px;display:flex;align-items:center;gap:9px;color:#ccc;font-family:'Raleway',sans-serif;font-size:9.5px}
.avatar{width:32px;height:32px;border-radius:50%;background:radial-gradient(circle at 50% 40%,#c9a58c,#5a4336)}
.caret{width:0;height:0;border-left:3px solid transparent;border-right:3px solid transparent;border-top:3px solid #ccc;margin-left:5px}
.sidebar{position:absolute;left:0;top:58px;width:161px;height:1094px;background:var(--sidebar);font-family:'Raleway',sans-serif}
.menu-toggle{position:absolute;left:10px;top:18px;width:26px;height:26px;background:#222;display:flex;flex-direction:column;justify-content:center;align-items:center;gap:2px}
.menu-toggle span{width:7px;height:1px;background:#888}
.nav{position:absolute;top:59px;left:0;width:174px;list-style:none}
.nav li{display:flex;align-items:center;gap:10px;height:27px;padding-left:14px;color:#fff;font-size:10px;font-weight:500}
.nav li.active{background:var(--teal);position:relative;width:161px;margin-bottom:4px}
.nav li.active::after{content:"";position:absolute;right:-13px;top:0;border-top:13.5px solid transparent;border-bottom:13.5px solid transparent;border-left:13px solid var(--teal)}
.nav li:not(.active){height:24px}
.footer{position:absolute;left:0;top:1152px;width:883px;height:48px;background:var(--footer);color:#666;font-size:7.5px}
.footer .copy{position:absolute;left:33px;top:21px}
.footer .top{position:absolute;left:823px;top:12px;width:24px;height:22px;background:#1a1a1a;color:#ddd;font-size:5.5px;text-align:center;padding-top:7px}
.crumb{position:absolute;left:183px;top:74px;width:669px;height:28px;background:var(--crumb);font-family:'Raleway',sans-serif;font-size:9px;color:#555;display:flex;align-items:center;padding-left:13px;gap:6px}
.card{position:absolute;top:118px;width:327px;height:103px;color:#fff;font-family:'Raleway',sans-serif}
.card .main{height:67px;position:relative}
.card .foot{height:36px;display:flex;align-items:center;justify-content:space-between;padding:0 13px 0 15px;font-size:8.5px;font-weight:500}
.card h2{position:absolute;right:15px;top:18px;font-weight:400;font-size:18.5px}
.card p{position:absolute;right:15px;top:43px;font-size:8.5px}
.card .ico{position:absolute;left:14px;top:12px}
.card.profile{left:183px}
.card.profile .main{background:var(--teal)}
.card.profile .foot{background:var(--teal-dark)}
.card.patients{left:525px}
.card.patients .main{background:var(--blue)}
.card.patients .foot{background:var(--blue-dark)}
.panel{position:absolute;width:327px;background:var(--panel-body)}
.panel .head{height:31px;background:var(--panel-head);color:#fff;font-family:'Raleway',sans-serif;font-weight:500;font-size:11.5px;display:flex;align-items:center;gap:8px;padding-left:13px}
.col-l{left:183px}.col-r{left:525px}
.welcome .sub{display:flex;align-items:center;gap:14px;padding:14px 13px 0}
.welcome h3{font-family:'Raleway',sans-serif;font-weight:500;font-size:11.5px;color:#333}
.badge{background:var(--green);color:#fff;font-size:8.5px;padding:5px 12px;font-family:'Raleway',sans-serif}
.welcome .body{padding:16px 13px 0;font-size:7.5px;line-height:15.2px;color:#666}
.legend{position:absolute;font-size:5.5px;color:#666;line-height:12px}
.legend i{display:inline-block;width:8px;height:5px;margin-right:2px;vertical-align:-1px}
.search{position:absolute;right:13px;top:44px;width:114px;height:21px;border:1px solid #ddd;background:#fff;font-size:6.5px;font-style:italic;color:#bbb;padding:6px 9px}
.search svg{position:absolute;right:7px;top:5px}
table{position:absolute;left:11px;top:79px;width:303px;border-collapse:collapse;font-size:7.5px;color:#666}
th{background:#ececec;height:22px;text-align:left;font-weight:400;color:#333;font-size:7.5px;font-family:'Raleway',sans-serif;padding-left:11px}
td{height:23px;padding-left:11px;border-bottom:1px solid #eee}
.sort{color:#aaa;font-size:6px;margin-left:3px}
.sort.up{color:#4a6fc0}
.info{position:absolute;left:13px;bottom:13px;color:var(--link);font-size:7.5px}
.pager{position:absolute;right:13px;bottom:12px;display:flex;font-size:7.5px}
.pager span{background:#ececec;padding:4px 5px;border-left:1px solid #ddd}
.pager .prev{color:#aaa;padding:4px 9px;border:0}
.pager .num{color:var(--link);background:#fff}
.pager .next{color:var(--link);background:#fff;padding:4px 9px}
.bar{display:inline-block;width:65px;height:8px;background:#eee;vertical-align:middle}
.bar b{display:block;height:8px;background:linear-gradient(90deg,#3cc6e0,#28b4d4)}
.star{color:var(--star);font-size:10px;letter-spacing:-1px}
.star .off{color:#bbb}
.prof{color:var(--link);font-size:7px}
</style>
</head>
<body>
<header class="topbar">
  <div class="user"><div class="avatar" role="img" aria-label="Profilfoto des angemeldeten Arztes"></div>Dr. Lenart<span class="caret"></span></div>
</header>

<aside class="sidebar">
  <div class="menu-toggle"><span></span><span></span><span></span></div>
  <ul class="nav">
    <li class="active"><svg width="10" height="9" viewBox="0 0 10 9"><path d="M5 0L0 4.5h1.3V9h2.6V6h2.2v3h2.6V4.5H10z" fill="#fff"/></svg>Dashboard</li>
    <li><svg width="8" height="9" viewBox="0 0 8 9"><circle cx="4" cy="2.3" r="2.2" fill="#fff"/><path d="M0 9c0-3 1.7-4.3 4-4.3S8 6 8 9z" fill="#fff"/></svg>Mein Konto</li>
    <li><svg width="8" height="9" viewBox="0 0 8 9"><circle cx="4" cy="2.3" r="2.2" fill="#fff"/><path d="M0 9c0-3 1.7-4.3 4-4.3S8 6 8 9z" fill="#fff"/></svg>Patientbewertungen</li>
  </ul>
</aside>

<div class="crumb"><svg width="10" height="9" viewBox="0 0 10 9"><path d="M5 0L0 4.5h1.3V9h2.6V6h2.2v3h2.6V4.5H10z" fill="#888"/></svg>Start ›</div>

<section class="card profile">
  <div class="main">
    <svg class="ico" width="38" height="44" viewBox="0 0 38 44" fill="none" stroke="#fff" stroke-width="2"><circle cx="19" cy="12" r="10"/><path d="M2 42v-8c0-6 5-10 11-10h12c6 0 11 4 11 10v8z"/></svg>
    <h2>Profile</h2><p>Profile bearbeiten</p>
  </div>
  <div class="foot">WEITER<svg width="12" height="12" viewBox="0 0 12 12"><circle cx="6" cy="6" r="5.5" fill="#fff"/><path d="M3 6h5M6 3.5L8.5 6 6 8.5" stroke="var(--teal-dark)" stroke-width="1.4" fill="none"/></svg></div>
</section>

<section class="card patients">
  <div class="main">
    <svg class="ico" width="50" height="48" viewBox="0 0 50 48" fill="none" stroke="#fff" stroke-width="2"><circle cx="12" cy="9" r="7"/><circle cx="38" cy="9" r="7"/><circle cx="25" cy="20" r="9"/><path d="M3 32v-5c0-4 3-7 7-7h4M47 32v-5c0-4-3-7-7-7h-4"/><path d="M10 46v-8c0-5 4-8 8-8h14c4 0 8 3 8 8v8z"/></svg>
    <h2>Patienten</h2><p>Patienten verwalten</p>
  </div>
  <div class="foot">ALLE ANSEHEN<svg width="12" height="12" viewBox="0 0 12 12"><circle cx="6" cy="6" r="5.5" fill="#fff"/><path d="M3 6h5M6 3.5L8.5 6 6 8.5" stroke="var(--blue-dark)" stroke-width="1.4" fill="none"/></svg></div>
</section>

<section class="panel col-l welcome" style="top:241px;height:181px">
  <div class="head"><svg width="10" height="10" viewBox="0 0 10 10" fill="none" stroke="#fff"><rect x="0.5" y="0.5" width="9" height="9"/><path d="M1 9l3-4 2 2 1.5-1.5L9 8"/></svg>Willkommen: Dr. Almeter</div>
  <div class="sub"><h3>Neque porro quisquam est dolorem</h3><span class="badge">Alles OK</span></div>
  <p class="body">Lorem ipsum dolor sit amet, consectetur adipiscing elit, sed do eiusmod tempor incididunt ut labore et dolore magna aliqua. Ut enim ad minim veniam, quis nos trud exercitation ullamco laboris nisi ut aliquip ex ea comm. Lorem ipsum dolor sit amet, consectetur adipiscing elit, sed do eiusmod tempor incididunt ut labore ullamco laboris nisi ut aliquip ex ea commodo consequat.</p>
</section>

<section class="panel col-r" style="top:241px;height:181px">
  <div class="head">Rankora Trend fur:</div>
  <svg width="327" height="150" viewBox="0 0 327 150" style="position:absolute;left:0;top:31px">
    <g stroke="#e4e4e4" stroke-width="0.6">
      <line x="0" x1="49" y1="0" x2="49" y2="0"/>
      <line x1="79" y1="10" x2="79" y2="131"/><line x1="109" y1="10" x2="109" y2="131"/><line x1="139" y1="10" x2="139" y2="131"/><line x1="169" y1="10" x2="169" y2="131"/><line x1="199" y1="10" x2="199" y2="131"/><line x1="229" y1="10" x2="229" y2="131"/><line x1="259" y1="10" x2="259" y2="131"/>
      <line x1="49" y1="50" x2="278" y2="50"/><line x1="49" y1="91" x2="278" y2="91"/>
    </g>
    <rect x="49" y="10" width="229" height="121" fill="none" stroke="#444" stroke-width="1"/>
    <polyline fill="none" stroke="#e8c56a" stroke-width="1.3" points="50,131 165,131 169,60 173,54 176,58 180,16 183,24 186,40 189,58 192,64 195,70 198,62 201,68 204,62 207,68 210,62 213,66 216,64 219,68 222,66 226,64 230,66 234,62 238,64 242,60 246,62 250,58 254,62 258,58 262,60 266,58 270,56 274,58 277,54"/>
    <g font-size="5.5" fill="#666" font-family="Open Sans,sans-serif">
      <text x="39" y="12">15</text><text x="39" y="52">10</text><text x="42" y="93">5</text><text x="42" y="133">0</text>
      <text x="68" y="144">Oct 2012</text><text x="98" y="144">Jan 2013</text><text x="128" y="144">Apr 2013</text><text x="159" y="144">Jul 2013</text><text x="188" y="144">Oct 2013</text><text x="218" y="144">Jan 2014</text><text x="247" y="144">Apr 2014</text>
    </g>
  </svg>
</section>

<section class="panel col-l" style="top:442px;height:180px">
  <div class="head">Pie: 1</div>
  <svg width="112" height="112" viewBox="-56 -56 112 112" style="position:absolute;left:82px;top:46px">
    <path d="M0 0L0 -54A54 54 0 0 1 10.3 53Z" fill="#ecc23f"/>
    <path d="M0 0L10.3 53A54 54 0 0 1 -39.5 36.8Z" fill="#b3d8f5"/>
    <path d="M0 0L-39.5 36.8A54 54 0 0 1 0 -54Z" fill="#cc4745"/>
  </svg>
  <div class="legend" style="left:240px;top:53px"><div><i style="background:#ecc23f"></i>Series1</div><div><i style="background:#b3d8f5"></i>Series2</div><div><i style="background:#cc4745"></i>Series3</div></div>
</section>

<section class="panel col-r" style="top:442px;height:180px">
  <div class="head">Pie: 2</div>
  <svg width="114" height="114" viewBox="-57 -57 114 114" style="position:absolute;left:86px;top:45px">
    <path d="M0 0L0 -55A55 55 0 0 1 13.4 -52.3Z" fill="#ecc23f"/>
    <path d="M0 0L13.4 -52.3A55 55 0 0 1 41.6 -34.4Z" fill="#b3d8f5"/>
    <path d="M0 0L41.6 -34.4A55 55 0 0 1 10.3 53Z" fill="#cc4745"/>
    <path d="M0 0L10.3 53A55 55 0 0 1 -53 10.3Z" fill="#4aaa4a"/>
    <path d="M0 0L-53 10.3A55 55 0 0 1 0 -55Z" fill="#9a3ee8"/>
  </svg>
  <div class="legend" style="left:246px;top:55px"><div><i style="background:#ecc23f"></i>Series1</div><div><i style="background:#b3d8f5"></i>Series2</div><div><i style="background:#cc4745"></i>Series3</div><div><i style="background:#4aaa4a"></i>Series4</div><div><i style="background:#9a3ee8"></i>Series5</div><div><i style="background:#c99a2a"></i>Series6</div></div>
</section>

<section class="panel col-l" style="top:642px;height:228px">
  <div class="head">Stat: 1</div>
  <div class="search">Search..<svg width="8" height="8" viewBox="0 0 8 8" fill="none" stroke="#666"><circle cx="3.2" cy="3.2" r="2.6"/><path d="M5.2 5.2L7.6 7.6"/></svg></div>
  <table>
    <tr><th>NAME<span class="sort up" style="margin-left:48px">▲</span></th><th>POSITION<span class="sort" style="margin-left:30px">⬍</span></th><th>START DATE<span class="sort" style="margin-left:26px">⬍</span></th><th>SALARY<span class="sort">⬍</span></th></tr>
    <tr><td>Gerda</td><td>Chefin</td><td>1.11.2013</td><td>Salami</td></tr>
    <tr><td>Gerda</td><td>Chefin</td><td>1.11.2013</td><td>Salami</td></tr>
    <tr><td>Gerda</td><td>Chefin</td><td>1.11.2013</td><td>Salami</td></tr>
    <tr><td>Gerda</td><td>Chefin</td><td>1.11.2013</td><td>Salami</td></tr>
  </table>
  <div class="info">Showing 1to5 of 9 entries</div>
  <div class="pager"><span class="prev">Previous</span><span>1</span><span class="num">2</span><span class="next">Next</span></div>
</section>

<section class="panel col-r" style="top:642px;height:228px">
  <div class="head">Stat: 2</div>
  <div class="search">Search..<svg width="8" height="8" viewBox="0 0 8 8" fill="none" stroke="#666"><circle cx="3.2" cy="3.2" r="2.6"/><path d="M5.2 5.2L7.6 7.6"/></svg></div>
  <table>
    <tr><th>DOMAIN<span class="sort up" style="margin-left:26px">▲</span> NIVEAU</th><th><span class="sort" style="margin-left:0">⬍</span> KEYW.</th><th><span class="sort">⬍</span> SE KEYW.<span class="sort">⬍</span></th></tr>
    <tr><td>domain1de. <span class="bar" style="margin-left:12px"><b style="width:6px"></b></span></td><td>Gemeninsame keyw.</td><td>SE Keywords</td></tr>
    <tr><td>domain2de. <span class="bar" style="margin-left:12px"><b style="width:15px"></b></span></td><td>Gemeninsame keyw.</td><td>SE Keywords</td></tr>
    <tr><td>domain3de. <span class="bar" style="margin-left:12px"><b style="width:30px"></b></span></td><td>Gemeninsame keyw.</td><td>SE Keywords</td></tr>
    <tr><td>domain4de. <span class="bar" style="margin-left:12px"><b style="width:44px"></b></span></td><td>Gemeninsame keyw.</td><td>SE Keywords</td></tr>
  </table>
  <div class="info">Showing 1to5 of 9 entries</div>
  <div class="pager"><span class="prev">Previous</span><span>1</span><span class="num">2</span><span class="next">Next</span></div>
</section>

<section class="panel col-l" style="top:892px;height:226px">
  <div class="head">Sternchen</div>
  <div class="search">Search..<svg width="8" height="8" viewBox="0 0 8 8" fill="none" stroke="#666"><circle cx="3.2" cy="3.2" r="2.6"/><path d="M5.2 5.2L7.6 7.6"/></svg></div>
  <table>
    <tr><th style="width:70px">NAME<span class="sort up" style="margin-left:48px">▲</span></th><th>PROFILSEITE</th><th>BEWERTUNG<span class="sort">⬍</span></th></tr>
    <tr><td>praxio.de.</td><td><span class="prof">› xyz ungelost</span></td><td><span class="star">★★★★<span class="off">☆</span></span></td></tr>
    <tr><td>praxio.de.</td><td><span class="prof">› xyz ungelost</span></td><td><span class="star">★★★★<span class="off">☆</span></span></td></tr>
    <tr><td>praxio.de.</td><td><span class="prof">› xyz ungelost</span></td><td><span class="star">★★★★<span class="off">☆</span></span></td></tr>
    <tr><td>praxio.de.</td><td><span class="prof">› xyz ungelost</span></td><td><span class="star">★★★★<span class="off">☆</span></span></td></tr>
  </table>
  <div class="info">Showing 1to5 of 9 entries</div>
  <div class="pager"><span class="prev">Previous</span><span>1</span><span class="num">2</span><span class="next">Next</span></div>
</section>

<footer class="footer">
  <span class="copy">2014 © Medirate</span>
  <div class="top">TOP</div>
</footer>
</body>
</html>
```